Pine Ridge Traders, LLC- Global Beverage Company with 100% Cold Chain Logistics

Hey All, My Name is Tom, I am a young business owner in a competitive export space, but my niche is that I am shipping all of my beer around the world, "100% Cold Chain". This model is more costly, but it protects the integrity of the beer itself and will give folks in foreign countries the best representation of what US Craft Beer has to offer.

I am not a branding guy and don't claim to be one, I am a salesperson first, and will be referring to all of you to create something great that will be memorable.

I am looking for a basic Business Card Design for my Craft Beer Export company. I sell US Craft Beer in several countries around the globe. Austrailia, China, Taiwan, Chile, France, New Zealand... to name a few.

I am looking for a sleek, modern, and fresh design. Quickly!

Thanks for your consideration!

Cheers,

Tom

Target Market(s)

International

Contact Information for Business Card

Tom Reilly
Founder- World Brew Guy
Tom@PineRidgeTraders.example
@WorldBrewGuy- Instagram only
www.Pineridgetraders.example
@PineRidgeTradersAU- Instagram Only

Font styles to use
Serif

Colors
0592cd
ffffff

Requirements
Must have
• Name-
• Title-
• Email-
• Social Media Handle-
• Company Website-
Nice to have
• Nice Logo/ Images on Card
Should not have
• Tacky Beer Images

```html
<!DOCTYPE html>
<html lang="en">
<head>
<meta charset="utf-8">
<title>Pine Ridge Traders – Business Card</title>
<link rel="stylesheet" href="https://fonts.googleapis.com/css2?family=Open+Sans:wght@400;600;700&display=swap">
<style>
  :root {
    --brand-blue: #0592cd;
    --brand-deep: #0b56a8;
    --brand-light: #0fb4dc;
    --paper: #ffffff;
    --stage: #eef1f4;
    --muted: #5a6b78;
  }
  * { margin: 0; padding: 0; box-sizing: border-box; }
  html, body { width: 1200px; height: 675px; overflow: hidden; }
  body {
    background: var(--stage);
    font-family: "Open Sans", sans-serif;
    position: relative;
  }
  .card {
    position: absolute;
    width: 520px;
    height: 297px;
    top: 189px;
    border-radius: 4px;
    box-shadow: 0 8px 24px rgba(0, 0, 0, 0.12);
    overflow: hidden;
  }
  .card-front {
    left: 50px;
    background: linear-gradient(200deg, var(--brand-light) 0%, var(--brand-blue) 45%, var(--brand-deep) 100%);
    display: flex;
    align-items: center;
    justify-content: center;
  }
  .brand-name {
    color: var(--paper);
    font-weight: 700;
    font-size: 32px;
    line-height: 1.2;
    white-space: nowrap;
  }
  .card-back {
    left: 630px;
    background: var(--paper);
  }
  .identity {
    position: absolute;
    right: 300px;
    top: 100px;
    text-align: right;
  }
  .person-name {
    color: var(--brand-blue);
    font-weight: 700;
    font-size: 20px;
    white-space: nowrap;
  }
  .person-title {
    color: var(--muted);
    font-size: 8px;
    white-space: nowrap;
  }
  .divider {
    position: absolute;
    left: 238px;
    top: 90px;
    width: 1px;
    height: 115px;
    background: var(--brand-blue);
  }
  .contact-list {
    position: absolute;
    left: 254px;
    top: 130px;
    list-style: none;
    color: var(--brand-blue);
    font-weight: 600;
    font-size: 12px;
    line-height: 1.9;
    white-space: nowrap;
  }
  .back-brand {
    position: absolute;
    right: 24px;
    top: 40px;
  }
  .back-brand .brand-name {
    color: var(--brand-blue);
    font-size: 14px;
  }
</style>
</head>
<body>
  <section class="card card-front" aria-label="Card front">
    <div class="brand-name">Pine Ridge Traders</div>
  </section>

  <section class="card card-back" aria-label="Card back">
    <div class="identity">
      <div class="person-name">Tom Reilly</div>
      <div class="person-title">Founder – World Brew Guy</div>
    </div>
    <div class="divider"></div>
    <ul class="contact-list">
      <li>Tom@PineRidgeTraders.example</li>
      <li>@WorldBrewGuy</li>
      <li>www.Pineridgetraders.example</li>
    </ul>
    <div class="back-brand">
      <div class="brand-name">Pine Ridge Traders</div>
    </div>
  </section>
</body>
</html>
```